Modern Billboard Ad for Criminal Defense Firm

10.5 x 36 We're looking for something to set us apart from the local competition. Looking for sleek and modern. We're a mid-sized firm in a small market city. We want to give the artist room to be creative on this one.
Thanks

Target Market(s)

Adult clients who have been charged with a crime/DWI

Industry/Entity Type

legal

Font styles to use
Serif
Sans Serif

Requirements
Must have
• Needs to have the firm name in large lettering. Law Offices of Marcus T Whitfield. “PLLC” does not have to be included. Phone number of (555) 384-1927 should be included but not the main focus.
Nice to have
• A call to action or something similar. “Don’t go it alone, call today.”, “ Arrested?”

```html
<!DOCTYPE html>
<html lang="en">
<head>
<meta charset="utf-8">
<title>Marcus T Whitfield – Criminal Defense Billboard</title>
<link href="https://fonts.googleapis.com/css2?family=Montserrat:wght@600;700;800&display=swap" rel="stylesheet">
<style>
  :root {
    --page-bg: #2b3f5c;
    --panel-black: #0b0b0c;
    --panel-white: #ffffff;
    --panel-grey: #cfcfd3;
    --brand-blue: #1a8fdb;
    --brand-blue-deep: #0f6fc0;
    --text-light: #e9e9ea;
    --text-dark: #121212;
    --photo-light: #9a9a9c;
    --photo-dark: #2a2a2c;
  }
  * { margin: 0; padding: 0; box-sizing: border-box; }
  html, body {
    width: 1200px;
    height: 900px;
    overflow: hidden;
    background: var(--page-bg);
  }
  .billboard {
    position: absolute;
    left: 30px;
    top: 307px;
    width: 1140px;
    height: 285px;
    overflow: hidden;
    font-family: "Montserrat", sans-serif;
    background: var(--panel-black);
  }
  .billboard svg { display: block; }
  .firm-intro { font-weight: 700; font-size: 32px; fill: var(--text-light); letter-spacing: 0.5px; }
  .firm-name { font-weight: 800; font-size: 39px; fill: var(--brand-blue); }
  .practice { font-weight: 700; font-size: 17px; fill: #ffffff; letter-spacing: 0.5px; }
  .headline { font-weight: 700; font-size: 48px; fill: var(--text-dark); }
  .cta { font-weight: 800; font-size: 38px; fill: var(--brand-blue); }
  .phone { font-weight: 700; font-size: 36px; fill: #f2f6fb; }
</style>
</head>
<body>
  <div class="billboard">
    <svg width="1140" height="285" viewBox="0 0 1140 285">
      <defs>
        <radialGradient id="glow" cx="0.55" cy="0.35" r="0.75">
          <stop offset="0" stop-color="var(--panel-white)"/>
          <stop offset="0.7" stop-color="#eeeef0"/>
          <stop offset="1" stop-color="var(--panel-grey)"/>
        </radialGradient>
        <linearGradient id="portraitTone" x1="0" y1="0" x2="1" y2="1">
          <stop offset="0" stop-color="var(--photo-light)"/>
          <stop offset="0.55" stop-color="#5e5e61"/>
          <stop offset="1" stop-color="var(--photo-dark)"/>
        </linearGradient>
        <linearGradient id="arrowFill" x1="0" y1="0" x2="1" y2="0">
          <stop offset="0" stop-color="var(--brand-blue)"/>
          <stop offset="1" stop-color="var(--brand-blue-deep)"/>
        </linearGradient>
      </defs>

      <!-- panels -->
      <rect class="panel-dark" x="0" y="0" width="640" height="285" fill="var(--panel-black)"/>
      <rect class="panel-light" x="620" y="0" width="520" height="285" fill="url(#glow)"/>

      <!-- portrait area -->
      <path class="portrait" role="img" aria-label="Black and white portrait of the attorney in a vest and tie, jacket over his shoulder"
            d="M530 0 L630 0 L650 140 L725 200 L725 285 L380 285 L420 180 L520 120 Z"
            fill="url(#portraitTone)"/>

      <!-- firm name -->
      <text class="firm-intro" x="255" y="61" text-anchor="middle">LAW OFFICES OF</text>
      <rect class="name-rule" x="0" y="70" width="510" height="2" fill="var(--brand-blue)"/>
      <text class="firm-name" x="255" y="115" text-anchor="middle">MARCUS T WHITFIELD</text>

      <!-- award badge -->
      <rect class="award-badge" x="35" y="155" width="73" height="102" fill="#1c5f93" stroke="#3aa0e0" stroke-width="2"/>

      <text class="practice" x="256" y="208" text-anchor="middle">CRIMINAL DEFENCE</text>

      <!-- call to action -->
      <text class="headline" x="905" y="88" text-anchor="middle">“ARRESTED?”</text>
      <text class="cta" x="912" y="201" text-anchor="middle">CALL TODAY.</text>

      <path class="phone-banner" d="M725 223 L1100 223 L1140 254 L1100 285 L725 285 Z" fill="url(#arrowFill)"/>
      <text class="phone" x="918" y="266" text-anchor="middle">(555) 384-1927</text>
    </svg>
  </div>
</body>
</html>
```